Industrial design for commercialization of products for cargo

Good morning, we need a website design divided into 4 sections for a newly created company. Torvelix means Industrial Products for Loading and Pumping. We are located in the capital of Mexico and distributed throughout the country. We sell a wide range of equipment and accessories, for handling and lifting of load: hoists, traction devices, trolleys, pulleys, cables, shackles, tensioners, rings, marine chains, among others, as well as pneumatic double diaphragm pumps And centrifugal pumps, used in the pharmaceutical, chemical, food, etc. industries. Our products are manufactured to the highest quality standards, most are manufactured in the United States. Recently, Artmosaic Hub (KALT.MERON) produced our company logo and we would like our website to be combined with it. We want the website to have an industrial design, that the colors combine with the logo and black letters. The images and information that we will use are in our current web page: www.torvelix-demo.com. If you need more information, please let us know. My name is Lidia Quevara and my email is ventastorvelix@mailbox-demo.net. Thank you. PD Please, I want the winner to upload to my server, the coded files html and CSS through FTP (File Transfer Protocol) I know this action means an extra cost, but I m willing to pay. Thanks.
Target Market(s)
Our market is very broad, among our clients are companies in the construction industry, manufacturing, as well as department stores, warehouses, even shops, seaports.
Industry/Entity Type
Commercial
Coding
Coded - Design and coding required
Number of Pages Required
5+ page
Font styles to use
Other font styles liked:
- Hay libertad en cuanto a la tipografía, pueden utilizar la que ustedes consideren conveniente.

Colors
Designer to choose colors to be used in the design.
Requirements
Must have
- The page that we want should be divided into the sections that you consider convenient. SECTION OF HOME INFORMATION.- Our data, biography, mission, vision, values, company address, telephone number, whatsapp, email and location map. PRODUCTS FOR LOADING. PRODUCTS FOR PUMPING. ACCESSORIES FOR LOADING. CONTACT.

Nice to have
- One design you can use as an example is the page of one of our suppliers: www.vultenor.com.mx, we would like our page to be better than that of this provider. We want you to have a better presentation. I would like them to use banners at the top and bottom where phone numbers are placed. I wish there was a space for the videos to run the products. My page must be in the Spanish language please. The choice of colors is at your discretion, however instead of the color orange, I would like them to use the color red.

Should not have
- My project should not seem unprofessional, but to show that we are a serious and important company. Do not look anything like our current page www.torvelix-demo.com We do not want the option to add to the shopping cart or a page with a catalog. Our page is just a means to promote our products. Sales are done by phone.

```html
<!DOCTYPE html>
<html lang="es">
<head>
<meta charset="utf-8">
<title>Torvelix · Productos Industriales para Carga y Bombeo</title>
<link href="https://fonts.googleapis.com/css2?family=Oswald:wght@400;500;600&family=Open+Sans:wght@400;600;700&display=swap" rel="stylesheet">
<style>
:root{
  --orange:#e2703a;
  --orange-dark:#cf5f2b;
  --charcoal:#3b3b3b;
  --panel-dark:#404040;
  --ink:#222;
  --text:#555;
  --light:#f4f4f4;
  --border:#e3e3e3;
  --footer:#1c1c1c;
  --white:#fff;
}
*{box-sizing:border-box;margin:0;padding:0}
html,body{width:1200px;height:3087px;overflow:hidden}
body{font-family:"Open Sans",Arial,sans-serif;color:var(--text);background:var(--white);position:relative}
.head{font-family:"Oswald","Arial Narrow",sans-serif;text-transform:uppercase}
.btn{display:inline-block;font-family:"Oswald","Arial Narrow",sans-serif;text-transform:uppercase;font-size:17px;font-weight:500;color:var(--white);background:var(--orange);padding:6px 24px;border-left:5px solid var(--charcoal)}
.btn.dark{background:var(--charcoal);border-left-color:var(--orange)}

/* header */
.site-header{height:118px;display:flex;align-items:center;justify-content:space-between;padding:0 82px 0 82px}
.brand{display:flex;align-items:center;gap:14px}
.brand-square{width:72px;height:72px;background:var(--orange)}
.brand-name{font-family:"Oswald",sans-serif;font-weight:600;font-size:44px;color:var(--charcoal);line-height:1;letter-spacing:1px}
.brand-tag{font-size:11px;font-weight:600;color:var(--charcoal);border-top:3px solid var(--orange);margin-top:4px;padding-top:3px}
.contact-top{display:flex;gap:30px}
.contact-item{display:flex;align-items:center;gap:10px}
.contact-item .ic{width:30px;height:30px;border-radius:50%;background:var(--orange);display:flex;align-items:center;justify-content:center}
.contact-item b{display:block;font-family:"Oswald",sans-serif;font-size:14px;color:var(--charcoal);letter-spacing:1px}
.contact-item span{font-size:12px;font-weight:600;color:var(--charcoal)}

/* nav */
.main-nav{height:47px;background:var(--charcoal);display:flex;padding-left:80px;padding-right:82px}
.main-nav a{flex:1;display:flex;align-items:center;justify-content:center;color:var(--white);text-decoration:none;font-family:"Oswald",sans-serif;font-size:15px;font-weight:500;text-transform:uppercase;border-right:1px solid #555}
.main-nav a.active{flex:0 0 113px;background:var(--orange)}
.main-nav a:last-child{border-right:none}

/* hero */
.hero{position:relative;height:487px;background:linear-gradient(120deg,#c9a377 0%,#e9a13a 22%,#b9b3a7 40%,#d7d0c5 60%,#8fa3c4 78%,#c9c2b6 100%)}
.hero-box{position:absolute;left:100px;top:180px;width:556px;height:175px;background:rgba(40,40,40,.85);padding:20px 0 0 0}
.hero-box h1{font-family:"Oswald",sans-serif;font-weight:500;font-size:38px;line-height:48px;color:var(--white);padding-left:0;margin-left:0;text-transform:uppercase}
.hero-box .btn{margin-top:14px;border-left:none;font-size:16px;padding:6px 16px}
.hero-dots{position:absolute;left:580px;top:448px;display:flex;gap:6px}
.hero-dots i{width:11px;height:11px;border-radius:50%;background:#555}
.hero-dots i.on{background:var(--orange)}

/* section titles */
.sec-title{text-align:center;font-family:"Oswald",sans-serif;font-size:30px;font-weight:500;text-transform:uppercase;color:var(--ink)}
.sec-title em{font-style:normal;color:var(--orange)}
.divider{display:flex;justify-content:center;margin-top:8px}

/* about */
.about{height:391px;padding-top:46px;text-align:center;position:relative}
.about .lead{width:1000px;margin:26px auto 0;font-size:13px;font-weight:700;color:var(--ink);line-height:20px}
.about .body{width:1040px;margin:18px auto 0;font-size:12.5px;line-height:22px;color:var(--text)}
.about .btn{margin-top:28px}

/* split panels */
.split{height:412px;display:flex;position:relative}
.split .panel{flex:1;text-align:center;padding-top:64px;color:var(--white)}
.split .left{background:var(--panel-dark)}
.split .right{background:var(--orange)}
.panel .badge{width:106px;height:106px;border-radius:50%;border:3px solid var(--white);margin:0 auto;display:flex;align-items:center;justify-content:center}
.left .badge{background:var(--orange)}
.right .badge{background:var(--charcoal)}
.panel h2{font-family:"Oswald",sans-serif;font-size:26px;font-weight:500;text-transform:uppercase;margin-top:22px}
.panel p{width:440px;margin:10px auto 0;font-size:13px;font-weight:600;line-height:23px}
.panel .btn{margin-top:24px}
.hub{position:absolute;left:532px;top:126px;width:132px;height:132px;border-radius:50%;background:var(--white);border:6px solid #ddd;display:flex;align-items:center;justify-content:center}
.hub span{width:64px;height:64px;background:var(--orange)}

/* products */
.featured{height:795px;padding-top:50px}
.grid{display:grid;grid-template-columns:repeat(4,240px);column-gap:24px;row-gap:30px;justify-content:center;margin-top:38px;padding-left:0}
.card{height:283px;border:1px solid var(--border);display:flex;flex-direction:column}
.card .shot{flex:1;margin:20px 50px}
.card .name{height:62px;background:var(--light);display:flex;align-items:center;justify-content:center;font-family:"Oswald",sans-serif;font-size:15px;font-weight:500;color:var(--ink);text-transform:uppercase}

/* cta */
.cta{height:267px;background:linear-gradient(90deg,#111 0%,#2a2a2a 45%,#1a1a1a 100%);text-align:center;color:var(--white);padding-top:60px}
.cta .small{font-family:"Oswald",sans-serif;font-size:25px;font-weight:500;text-transform:uppercase}
.cta .big{font-family:"Oswald",sans-serif;font-size:40px;font-weight:500;text-transform:uppercase;line-height:48px}
.cta .btn{margin-top:20px;font-size:17px;border-left:none}

/* partners */
.partners{height:206px;background:var(--white);display:flex;align-items:center;justify-content:center;gap:26px}
.partners .arrow{color:#999;font-size:30px;font-family:"Oswald",sans-serif}
.partner{width:150px;height:90px;border:1px solid var(--border);display:flex;align-items:center;justify-content:center}
.partner span{width:96px;height:34px;border-radius:4px;background:#d5d5d5}

/* footer */
.site-footer{height:315px;background:var(--footer);display:flex;padding:44px 0 0 82px;color:#ddd}
.col h4{font-family:"Oswald",sans-serif;font-size:20px;font-weight:500;text-transform:uppercase;color:var(--white);margin-bottom:20px}
.col h4 em{font-style:normal;color:var(--orange)}
.links{width:264px}
.links li{list-style:none;font-size:13px;line-height:38px;text-transform:uppercase}
.links li::before{content:"";display:inline-block;width:5px;height:5px;border-radius:50%;background:var(--orange);margin-right:10px;vertical-align:middle}
.detail{width:324px;font-size:13px;line-height:20px}
.detail b{display:block;color:var(--white)}
.detail .row{display:flex;gap:10px;align-items:center;margin-top:14px}
.quick{width:330px}
.quick .field{width:268px;height:34px;background:var(--white);margin-bottom:10px;font-size:12px;color:#999;padding:9px 10px}
.quick .submit{display:inline-block;background:var(--orange);color:var(--white);font-size:14px;font-weight:600;padding:6px 26px}
.follow li{list-style:none;display:flex;align-items:center;gap:12px;font-size:12px;font-weight:600;text-transform:uppercase;margin-bottom:13px;color:var(--white)}
.follow i{width:30px;height:30px;border-radius:50%;background:#555;display:block}
.copyright{height:49px;background:var(--orange);color:var(--white);font-size:13px;font-weight:600;display:flex;align-items:center;justify-content:center}
</style>
</head>
<body>

<header class="site-header">
  <div class="brand">
    <div class="brand-square"></div>
    <div>
      <div class="brand-name">TORVELIX</div>
      <div class="brand-tag">Productos Industriales Para Carga y Bombeo</div>
    </div>
  </div>
  <div class="contact-top">
    <div class="contact-item">
      <div class="ic"><svg width="16" height="16" viewBox="0 0 24 24"><path fill="#fff" d="M6.6 10.8a15 15 0 0 0 6.6 6.6l2.2-2.2a1 1 0 0 1 1-.25 11.4 11.4 0 0 0 3.6.57 1 1 0 0 1 1 1V20a1 1 0 0 1-1 1A17 17 0 0 1 3 4a1 1 0 0 1 1-1h3.5a1 1 0 0 1 1 1c0 1.25.2 2.45.57 3.6a1 1 0 0 1-.25 1z"/></svg></div>
      <div><b>CALL US :</b><span>01 55 4810 2309</span></div>
    </div>
    <div class="contact-item">
      <div class="ic"><svg width="16" height="16" viewBox="0 0 24 24"><path fill="#fff" d="M3 5h18v14H3z"/><path fill="none" stroke="#e2703a" stroke-width="2" d="M3 5l9 7 9-7"/></svg></div>
      <div><b>MAIL US :</b><span>ventastorvelix@mailbox-demo.net</span></div>
    </div>
  </div>
</header>

<nav class="main-nav">
  <a class="active">Inicio</a>
  <a>Productos para carga</a>
  <a>Productos para bombeo</a>
  <a>Accesorios</a>
  <a>Contacto</a>
</nav>

<section class="hero" role="img" aria-label="Polipasto eléctrico azul con gancho amarillo montado sobre viga naranja en nave industrial">
  <div class="hero-box">
    <h1 style="padding-left:0"><span style="display:block;padding-left:0;margin-left:-0px">&nbsp;WE SELL INDUSTRIAL PRODUCTS</span><span style="display:block">&nbsp;FOR LOADING &amp; PUMPING</span></h1>
    <span class="btn">Read more</span>
  </div>
  <div class="hero-dots"><i></i><i class="on"></i><i></i></div>
</section>

<section class="about">
  <h2 class="sec-title"><em>About</em> Torvelix productos industriales para carga y bombeo</h2>
  <div class="divider"><svg width="150" height="24" viewBox="0 0 150 24"><line x1="0" y1="12" x2="62" y2="12" stroke="#bbb"/><line x1="88" y1="12" x2="150" y2="12" stroke="#bbb"/><circle cx="75" cy="12" r="9" fill="none" stroke="#999" stroke-width="2"/></svg></div>
  <p class="lead">TORVELIX Productos Industriales Para Carga y Bombeo, somos una empresa dedicada a vender productos para carga: Polipastos de las marcas KORVAN, BRELTON y DUNMARK, fabricados en EEUU y México., con los más altos estándares de Calidad.</p>
  <p class="body">Eslingas de Cadena y Poliéster Marca Halvard y Accesorios para carga Marca Strelk. También comercializamos Bombas Neumáticas de Doble Diafragma, Bombas Eléctricas, Bombas Centrífugas Horizontales y Verticales, Bombas Dosificadoras entre otras. Manejamos marcas reconocidas PRANTEX, FLUXORA, MERIDALE, QUENTRA, OSVANE, VORDEX, TELLMAR, etc. Contamos con Fichas Técnicas y Manuales de Operación para todos nuestros productos. Haba para proporcionarle la información.</p>
  <span class="btn">Read more</span>
</section>

<section class="split">
  <div class="panel left">
    <div class="badge"><svg width="50" height="56" viewBox="0 0 50 56"><rect x="12" y="2" width="26" height="16" rx="3" fill="none" stroke="#fff" stroke-width="4"/><path d="M25 18v14a10 10 0 1 1-10 10" fill="none" stroke="#fff" stroke-width="5" stroke-linecap="round"/></svg></div>
    <h2>Productos para carga</h2>
    <p>Lorem ipsum dolor sit amet, consectetuer adipiscing elit, seddiam nonummy nibh euismod tincidunt ut laoreetfgf doloremagna aliquam erat volutpat.</p>
    <span class="btn">Read more</span>
  </div>
  <div class="hub"><span></span></div>
  <div class="panel right">
    <div class="badge"><svg width="54" height="54" viewBox="0 0 54 54"><circle cx="27" cy="27" r="22" fill="none" stroke="#fff" stroke-width="4"/><circle cx="27" cy="27" r="6" fill="#fff"/><path d="M27 8v12M27 34v12M8 27h12M34 27h12" stroke="#fff" stroke-width="4"/></svg></div>
    <h2>Productos para bombeo</h2>
    <p>Lorem ipsum dolor sit amet, consectetuer adipiscing elit, seddiam nonummy nibh euismod tincidunt ut laoreetfgf doloremagna aliquam erat volutpat.</p>
    <span class="btn dark">Read more</span>
  </div>
</section>

<section class="featured">
  <h2 class="sec-title"><em>Featured</em> products</h2>
  <div class="divider"><svg width="150" height="24" viewBox="0 0 150 24"><line x1="0" y1="12" x2="62" y2="12" stroke="#bbb"/><line x1="88" y1="12" x2="150" y2="12" stroke="#bbb"/><circle cx="75" cy="12" r="9" fill="none" stroke="#999" stroke-width="2"/></svg></div>
  <div class="grid">
    <div class="card"><div class="shot" role="img" aria-label="Polipasto eléctrico amarillo" style="background:radial-gradient(circle,#e6d52c 30%,#fff 72%)"></div><div class="name">TX-TITAN</div></div>
    <div class="card"><div class="shot" role="img" aria-label="Polipasto manual de cadena naranja" style="background:radial-gradient(ellipse 25% 50%,#d9703a 30%,#fff 90%)"></div><div class="name">TX-CICLÓN</div></div>
    <div class="card"><div class="shot" role="img" aria-label="Tecle de palanca amarillo" style="background:radial-gradient(ellipse 30% 50%,#e8c21f 30%,#fff 90%)"></div><div class="name">TX 650</div></div>
    <div class="card"><div class="shot" role="img" aria-label="Polipasto eléctrico de cadena naranja" style="background:radial-gradient(ellipse 35% 50%,#e45b33 35%,#fff 90%)"></div><div class="name">TX-LODEMAX</div></div>
    <div class="card"><div class="shot" role="img" aria-label="Polipasto manual amarillo con cadena" style="background:radial-gradient(ellipse 25% 50%,#e8c21f 25%,#fff 90%)"></div><div class="name">TX-620</div></div>
    <div class="card"><div class="shot" role="img" aria-label="Polipasto eléctrico negro y rojo" style="background:radial-gradient(ellipse 35% 40%,#222 35%,#fff 90%)"></div><div class="name">TX-VALOR</div></div>
    <div class="card"><div class="shot" role="img" aria-label="Polipasto de cable azul" style="background:radial-gradient(ellipse 40% 40%,#2f4c8a 35%,#fff 90%)"></div><div class="name">KORVAN K-80</div></div>
    <div class="card"><div class="shot" role="img" aria-label="Polipasto neumático rojo" style="background:radial-gradient(ellipse 25% 45%,#d9493a 25%,#fff 90%)"></div><div class="name">TX-AIRLIFT 6</div></div>
  </div>
</section>

<section class="cta" role="img" aria-label="Mano y engranajes industriales en tonos oscuros">
  <div class="small">Appreciate our prices, call now !!</div>
  <div class="big">We distribute throughout the Mexican Republic.</div>
  <span class="btn">Telephone : (01 55) 4810 2309</span>
</section>

<section class="partners">
  <span class="arrow">«</span>
  <div class="partner"><span></span></div>
  <div class="partner"><span></span></div>
  <div class="partner"><span></span></div>
  <div class="partner"><span></span></div>
  <div class="partner"><span></span></div>
  <div class="partner"><span></span></div>
  <span class="arrow">»</span>
</section>

<footer class="site-footer">
  <div class="col links">
    <h4>Quick <em>links</em></h4>
    <ul><li>Inicio</li><li>Productos para carga</li><li>Productos para bombeo</li><li>Accesorios</li><li>Contacto</li></ul>
  </div>
  <div class="col detail">
    <h4>Contact <em>detail</em></h4>
    <b>TORVELIX</b>
    <div>AV. PALMERAS DEL NORTE 418 INTERIOR 2<br>Col. Lomas de Arce Delegación Sierra Alta<br>Ciudad de México</div>
    <div class="row"><svg width="14" height="14" viewBox="0 0 24 24"><path fill="#e2703a" d="M6.6 10.8a15 15 0 0 0 6.6 6.6l2.2-2.2a1 1 0 0 1 1-.25 11.4 11.4 0 0 0 3.6.57 1 1 0 0 1 1 1V20a1 1 0 0 1-1 1A17 17 0 0 1 3 4a1 1 0 0 1 1-1h3.5a1 1 0 0 1 1 1c0 1.25.2 2.45.57 3.6a1 1 0 0 1-.25 1z"/></svg>01 55 4810 2309</div>
    <div class="row"><svg width="14" height="14" viewBox="0 0 24 24"><rect x="2" y="5" width="20" height="14" fill="#e2703a"/><path d="M2 5l10 7 10-7" fill="none" stroke="#1c1c1c" stroke-width="2"/></svg>ventastorvelix@mailbox-demo.net</div>
  </div>
  <div class="col quick">
    <h4>Quick <em>contact</em></h4>
    <div class="field">Name</div>
    <div class="field">Email</div>
    <div class="field">Message</div>
    <span class="submit">Submit</span>
  </div>
  <div class="col follow">
    <h4>Follow <em>us</em></h4>
    <ul><li><i></i>Friendsly</li><li><i></i>Chirper</li><li><i></i>Linkwork</li><li><i></i>Vidstream</li></ul>
  </div>
</footer>
<div class="copyright">Copyright © 2017 TORVELIX PRODUCTOS INDUSTRIALES PARA CARGA Y BOMBEO. All Rights Reserved.</div>

</body>
</html>
```